BRV Business Cards
Business Cards
BRV Business Cards - Security
Creative Brief
Professional
Daniel Forster
President
742 Larkfield Road Edison, NJ 08841
d.forster@brv-inc.example
www.brv-inc.example

```html
<!DOCTYPE html>
<html lang="en">
<head>
<meta charset="utf-8">
<title>BRV Business Cards</title>
<link rel="stylesheet" href="https://fonts.googleapis.com/css2?family=Crimson+Text:wght@400;600;700&display=swap">
<style>
:root{
  --page:#e9e6e1;
  --card:#ffffff;
  --navy:#0d2a66;
  --navy-deep:#061a45;
  --navy-light:#2a5bb8;
  --silver:#9a9ea6;
  --ink:#1d3f86;
  --white:#ffffff;
}
*{margin:0;padding:0;box-sizing:border-box}
html,body{width:1200px;height:852px;overflow:hidden;background:var(--page)}
body{position:relative;font-family:"Crimson Text",Georgia,serif}
.card{position:absolute;width:560px;height:320px;border-radius:18px;overflow:hidden;background:var(--card)}
.card--front{left:50px;top:90px}
.card--back{left:590px;top:440px}
.card__shapes{position:absolute;inset:0}
.brand{position:absolute;display:flex;align-items:center;gap:10px}
.brand__dot{width:36px;height:36px;border-radius:50%;background:var(--navy);flex:none}
.brand__name{font-weight:600;font-size:20px;line-height:1.02;color:var(--ink);letter-spacing:.5px;white-space:nowrap}
.card--front .brand{left:22px;top:104px}
.card--back .brand{left:318px;top:40px}
.person{position:absolute;color:var(--white)}
.person__name{font-weight:700;font-size:21px;line-height:1.1}
.person__title{font-weight:700;font-size:14px}
.card--front .person{right:26px;top:26px;text-align:right}
.card--back .person{left:26px;top:90px}
.address{position:absolute;color:var(--white);font-size:13px;line-height:1.35}
.card--front .address{right:28px;top:124px;text-align:right;width:170px}
.card--back .address{left:26px;top:172px;width:170px}
.contacts{position:absolute;list-style:none;color:var(--white);font-size:13px;line-height:1}
.contacts li{display:flex;align-items:center;gap:8px;height:19px;white-space:nowrap}
.contacts svg{width:12px;height:12px;flex:none}
.card--front .contacts{right:24px;top:202px}
.card--front .contacts li{justify-content:flex-end}
.card--back .contacts{left:24px;top:224px}
</style>
</head>
<body>

<section class="card card--front" aria-label="Business card, front">
  <svg class="card__shapes" viewBox="0 0 560 320" width="560" height="320">
    <defs>
      <radialGradient id="blueGlowFront" cx="0.62" cy="0.45" r="0.7">
        <stop offset="0" stop-color="var(--navy-light)"/>
        <stop offset="0.55" stop-color="var(--navy)"/>
        <stop offset="1" stop-color="var(--navy-deep)"/>
      </radialGradient>
    </defs>
    <path d="M282,0 C228,110 200,230 150,320 L178,320 C226,230 252,110 304,0 Z" fill="var(--silver)"/>
    <path d="M304,0 C252,110 226,230 178,320 L560,320 L560,0 Z" fill="url(#blueGlowFront)"/>
  </svg>
  <div class="brand"><span class="brand__dot"></span><span class="brand__name">BASTION<br>RIDGE<br>VIGILANCE</span></div>
  <div class="person"><p class="person__name">Daniel Forster</p><p class="person__title">President</p></div>
  <p class="address">742 Larkfield Road<br>Edison, NJ 08841</p>
  <ul class="contacts">
    <li>732-555-0141 <svg viewBox="0 0 12 12"><path d="M2.5 1h2l1 3-1.5 1a6 6 0 0 0 3 3l1-1.5 3 1v2a1 1 0 0 1-1 1A10 10 0 0 1 1.5 2a1 1 0 0 1 1-1z" fill="var(--white)"/></svg></li>
    <li>732-555-0142 <svg viewBox="0 0 12 12"><rect x="3" y="1" width="6" height="3" fill="var(--white)"/><rect x="1" y="4.5" width="10" height="4.5" rx="1" fill="var(--white)"/><rect x="3" y="8" width="6" height="3" fill="var(--white)"/></svg></li>
    <li>d.forster@brv-inc.example <svg viewBox="0 0 12 12"><rect x="1" y="2.5" width="10" height="7" fill="var(--white)"/><path d="M1 2.5l5 4 5-4" stroke="var(--navy)" fill="none"/></svg></li>
    <li>www.brv-inc.example <svg viewBox="0 0 12 12"><circle cx="6" cy="6" r="5" fill="none" stroke="var(--white)"/><path d="M1 6h10M6 1c-3 3-3 7 0 10M6 1c3 3 3 7 0 10" stroke="var(--white)" fill="none" stroke-width=".8"/></svg></li>
  </ul>
</section>

<section class="card card--back" aria-label="Business card, back">
  <svg class="card__shapes" viewBox="0 0 560 320" width="560" height="320">
    <defs>
      <radialGradient id="blueGlowBack" cx="0.35" cy="0.5" r="0.7">
        <stop offset="0" stop-color="var(--navy-light)"/>
        <stop offset="0.55" stop-color="var(--navy)"/>
        <stop offset="1" stop-color="var(--navy-deep)"/>
      </radialGradient>
    </defs>
    <path d="M250,0 C300,110 340,250 470,320 L500,320 C370,250 330,110 276,0 Z" fill="var(--silver)"/>
    <path d="M0,0 L250,0 C300,110 340,250 470,320 L0,320 Z" fill="url(#blueGlowBack)"/>
  </svg>
  <div class="brand"><span class="brand__dot"></span><span class="brand__name">BASTION<br>RIDGE<br>VIGILANCE</span></div>
  <div class="person"><p class="person__name">Daniel Forster</p><p class="person__title">President</p></div>
  <p class="address">742 Larkfield Road<br>Edison, NJ 08841</p>
  <ul class="contacts">
    <li><svg viewBox="0 0 12 12"><path d="M2.5 1h2l1 3-1.5 1a6 6 0 0 0 3 3l1-1.5 3 1v2a1 1 0 0 1-1 1A10 10 0 0 1 1.5 2a1 1 0 0 1 1-1z" fill="var(--white)"/></svg> 732-555-0141</li>
    <li><svg viewBox="0 0 12 12"><rect x="3" y="1" width="6" height="3" fill="var(--white)"/><rect x="1" y="4.5" width="10" height="4.5" rx="1" fill="var(--white)"/><rect x="3" y="8" width="6" height="3" fill="var(--white)"/></svg> 732-555-0142</li>
    <li><svg viewBox="0 0 12 12"><rect x="1" y="2.5" width="10" height="7" fill="var(--white)"/><path d="M1 2.5l5 4 5-4" stroke="var(--navy)" fill="none"/></svg> d.forster@brv-inc.example</li>
    <li><svg viewBox="0 0 12 12"><circle cx="6" cy="6" r="5" fill="none" stroke="var(--white)"/><path d="M1 6h10M6 1c-3 3-3 7 0 10M6 1c3 3 3 7 0 10" stroke="var(--white)" fill="none" stroke-width=".8"/></svg> www.brv-inc.example</li>
  </ul>
</section>

</body>
</html>
```